Update our business cards to match our awesome new website

Need a new design for company business cards. We have recently revamped our website and would like our business cards to get a refresh too. I've uploaded the company artwork, logo, as well as the Branding Deck to better understand the look & feel of our brand. Please visit the website at bellcrestholdingsoh.com.

Industry/Entity Type

Real Estate

Contact Information for Business Card

must use the colors outlined in the Branding Deck uploaded to the site, or the colors of our logo.

Font styles to use
Other font styles liked:
• Calibri

Requirements
Must have
• Required items: Name, title, company logo, address: 217 Fennimore Ave. Suite 300, Lakeport, OH 44093, email address: glen@bellcrestholdingsOH.com, company phone 800-555-0172, cell: 216-555-0148
Nice to have
• a more simple design. not complicated
Should not have
• cartoonish characters, or whimsical writing or artwork, stay within our branding colors

```html
<!DOCTYPE html>
<html lang="en">
<head>
<meta charset="utf-8">
<title>Bellcrest Holdings — Business Card, Design 1</title>
<link rel="stylesheet" href="https://fonts.googleapis.com/css2?family=Arimo:wght@400&family=Carlito&display=swap">
<style>
  :root {
    --canvas: #ffffff;
    --ink: #231f20;
    --card-border: #3a3a3a;
    --icon-blue: #1f6dbf;
    --brand-green: #6aaa35;
  }
  * { box-sizing: border-box; margin: 0; padding: 0; }
  html, body {
    width: 1200px; height: 675px; overflow: hidden;
    background: var(--canvas);
    font-family: "Arimo", Arial, sans-serif;
    color: var(--ink);
  }
  .sheet { position: relative; width: 1200px; height: 675px; }
  .sheet-title {
    position: absolute; top: 44px; left: 0; width: 100%;
    text-align: center; font-family: "Carlito", "Arimo", sans-serif;
    font-size: 27px; font-weight: 400; letter-spacing: 0.5px;
  }
  .card {
    position: absolute; left: 380px; width: 440px; height: 251px;
    border: 1px solid var(--card-border); background: #fff;
  }
  .card--back { top: 100px; }
  .card--front { top: 386px; }

  .brand {
    position: absolute; display: flex; align-items: center; gap: 7px;
    font-size: 15px; letter-spacing: 1px; text-transform: uppercase;
    color: var(--ink); white-space: nowrap;
  }
  .brand-dot { width: 11px; height: 11px; border-radius: 50%; background: var(--brand-green); flex: none; }
  .card--back .brand { top: 58px; right: 28px; }
  .card--front .brand { top: 146px; left: 0; width: 100%; justify-content: center; font-size: 26px; gap: 12px; }
  .card--front .brand-dot { width: 18px; height: 18px; }

  .holder { position: absolute; left: 26px; top: 72px; }
  .holder-name { font-size: 17.5px; line-height: 1.1; }
  .holder-role { font-size: 11.5px; letter-spacing: 0.3px; text-transform: uppercase; margin-top: 3px; }

  .contact { position: absolute; left: 22px; top: 124px; list-style: none; font-size: 11.5px; line-height: 15px; }
  .contact li { display: flex; align-items: flex-start; gap: 7px; }
  .contact svg { width: 13px; height: 13px; flex: none; margin-top: 1px; fill: var(--icon-blue); }
  .contact .gap { margin-top: 12px; }
  .contact .gap-sm { margin-top: 9px; }
  .contact .tight { margin-top: 2px; }
</style>
</head>
<body>
<main class="sheet">
  <h1 class="sheet-title">DESIGN 1</h1>

  <section class="card card--back" aria-label="Card back with contact details">
    <div class="brand"><span class="brand-dot"></span>Bellcrest Holdings</div>

    <div class="holder">
      <p class="holder-name">Glen Marlowe</p>
      <p class="holder-role">Managing Director</p>
    </div>

    <ul class="contact">
      <li>
        <svg viewBox="0 0 16 16" aria-hidden="true"><path d="M8 0a5.5 5.5 0 0 0-5.5 5.5C2.5 9.6 8 16 8 16s5.5-6.4 5.5-10.5A5.5 5.5 0 0 0 8 0zm0 8a2.5 2.5 0 1 1 0-5 2.5 2.5 0 0 1 0 5z"/></svg>
        <span>217 Fennimore Ave. Suite<br>300, Lakeport, OH 44093</span>
      </li>
      <li class="gap">
        <svg viewBox="0 0 16 16" aria-hidden="true"><path d="M1 6c0-2 3-3.5 7-3.5S15 4 15 6v1.2h-3.2V5.6c-1-.4-2.4-.6-3.8-.6s-2.8.2-3.8.6v1.6H1zM4.5 8h7l2 5.5h-11zM8 9.3a1.7 1.7 0 1 0 0 3.4 1.7 1.7 0 0 0 0-3.4z"/></svg>
        <span>800-555-0172</span>
      </li>
      <li class="tight">
        <svg viewBox="0 0 16 16" aria-hidden="true"><path d="M4.5 0h7A1.5 1.5 0 0 1 13 1.5v13a1.5 1.5 0 0 1-1.5 1.5h-7A1.5 1.5 0 0 1 3 14.5v-13A1.5 1.5 0 0 1 4.5 0zm.3 1.8v12.4h6.4V1.8z"/></svg>
        <span>216-555-0148</span>
      </li>
      <li class="gap-sm">
        <svg viewBox="0 0 16 16" aria-hidden="true"><path d="M0 3h16v1.2L8 9 0 4.2zm0 2.6 8 4.8 8-4.8V13H0z"/></svg>
        <span>glen@bellcrestholdingsOH.com</span>
      </li>
      <li class="tight">
        <svg viewBox="0 0 16 16" aria-hidden="true"><path d="M8 0a8 8 0 1 0 0 16A8 8 0 0 0 8 0zm5.9 7.2h-2.7a12 12 0 0 0-.9-4.9 6.4 6.4 0 0 1 3.6 4.9zM8 1.6c.8 1 1.5 3 1.6 5.6H6.4C6.5 4.6 7.2 2.6 8 1.6zM5.7 2.3a12 12 0 0 0-.9 4.9H2.1a6.4 6.4 0 0 1 3.6-4.9zM2.1 8.8h2.7c.1 1.9.4 3.6.9 4.9a6.4 6.4 0 0 1-3.6-4.9zM8 14.4c-.8-1-1.5-3-1.6-5.6h3.2c-.1 2.6-.8 4.6-1.6 5.6zm2.3-.7c.5-1.3.8-3 .9-4.9h2.7a6.4 6.4 0 0 1-3.6 4.9z"/></svg>
        <span>www.bellcrestholdingsOH.com</span>
      </li>
    </ul>
  </section>

  <section class="card card--front" aria-label="Card front with company name">
    <div class="brand"><span class="brand-dot"></span>Bellcrest Holdings</div>
  </section>
</main>
</body>
</html>
```